Business Card for a Jewellery Brand

Business card for an upscale jewellery brand. Attached is the brand logo and icon and color board. I am looking for two card versions: one for the founder and one is generic. The card should be elegant and convey upscale and premium feel. I am open to both square and rectangle card shapes.

Industry/Entity Type

Jewelry

Contact Information for Business Card

Two cards: (1) Sunila Perumbadi (Founder) (2) General
(1) Sunila Perumbadi card should have Name: Sunila Perumbadi, Title: Founder Email id: sunila@quelm.com.au. Phone no: +61412555307
(2) Generic card should have Email id: info@quelm.com.au. Phone no: +61431555962

Requirements
Must have
• Workmark
• ICON
• Phone no
• Email ID
• ABN: 48917205563 (Note: ABN is Business number in Australia)
• Website: www.quelm.com.au
• Instagram: quelm_jewellery
• Facebook: @quelmjewellery
Nice to have
• Tagline

```html
<!DOCTYPE html>
<html lang="en">
<head>
<meta charset="utf-8">
<title>Quelm Business Cards</title>
<link href="https://fonts.googleapis.com/css2?family=Montserrat:wght@300;400;500;600&display=swap" rel="stylesheet">
<style>
  :root {
    --rose: #e59a94;
    --white: #ffffff;
    --backdrop: #ece8e6;
  }
  * { margin: 0; padding: 0; box-sizing: border-box; }
  html, body { width: 1200px; height: 900px; overflow: hidden; }
  body {
    background: var(--backdrop);
    position: relative;
    font-family: "Montserrat", sans-serif;
  }
  .card { position: absolute; }
  .card--founder {
    left: 78px; top: 35px; width: 587px; height: 362px;
    background: var(--rose);
    color: var(--white);
  }
  .card--brand {
    left: 388px; top: 505px; width: 567px; height: 352px;
    background: var(--white);
    box-shadow: 0 2px 10px rgba(0,0,0,0.08);
  }
  .founder-name {
    position: absolute; left: 31px; top: 47px;
    font-size: 19px; font-weight: 600; letter-spacing: 0.02em;
    text-transform: uppercase; white-space: nowrap;
  }
  .founder-title {
    position: absolute; left: 31px; top: 72px;
    font-size: 15px; font-weight: 400;
  }
  .abn {
    position: absolute; left: 31px; top: 102px;
    font-size: 15px; font-weight: 400;
  }
  .contact-list, .social-list {
    position: absolute; left: 32px; list-style: none;
  }
  .contact-list { top: 191px; }
  .social-list { top: 268px; }
  .contact-list li, .social-list li {
    display: flex; align-items: center; gap: 7px;
    font-size: 14.5px; font-weight: 400; line-height: 21.5px;
    white-space: nowrap;
  }
  .social-list li { line-height: 26px; font-size: 15px; }
  .contact-icon { width: 11px; height: 11px; fill: var(--white); flex: none; }
  .social-dot {
    width: 21px; height: 21px; border-radius: 50%;
    background: var(--white); flex: none;
  }
  .founder-wordmark {
    position: absolute; left: 250px; top: 0; width: 337px; height: 362px;
    display: flex; align-items: center; justify-content: center;
    font-size: 58px; font-weight: 500; letter-spacing: 0.18em;
    padding-left: 0.18em;
  }
  .brand-lockup {
    position: absolute; left: 0; top: 0; width: 100%; height: 100%;
    display: flex; flex-direction: column; align-items: center; justify-content: center;
    gap: 24px; padding-top: 30px;
  }
  .brand-mark {
    width: 60px; height: 60px; border-radius: 50%;
    border: 4px solid var(--rose);
  }
  .brand-wordmark {
    color: var(--rose);
    font-size: 48px; font-weight: 400; letter-spacing: 0.32em;
    padding-left: 0.32em;
  }
</style>
</head>
<body>

<section class="card card--founder">
  <h1 class="founder-name">Sunila Perumbadi</h1>
  <p class="founder-title">Founder</p>
  <p class="abn">ABN: 48917205563</p>

  <ul class="contact-list">
    <li>
      <svg class="contact-icon" viewBox="0 0 24 24" aria-hidden="true"><path d="M6.6 10.8c1.4 2.8 3.8 5.1 6.6 6.6l2.2-2.2c.3-.3.7-.4 1-.2 1.1.4 2.3.6 3.6.6.6 0 1 .4 1 1V20c0 .6-.4 1-1 1C10.6 21 3 13.4 3 4c0-.6.4-1 1-1h3.5c.6 0 1 .4 1 1 0 1.3.2 2.5.6 3.6.1.3 0 .7-.2 1z"/></svg>
      +61412555307
    </li>
    <li>
      <svg class="contact-icon" viewBox="0 0 24 24" aria-hidden="true"><path d="M2 5h20v14H2z"/><path d="M3 6.5l9 6.5 9-6.5" fill="none" stroke="var(--rose)" stroke-width="1.6"/></svg>
      sunila@quelm.com.au.
    </li>
    <li>
      <svg class="contact-icon" viewBox="0 0 24 24" aria-hidden="true"><circle cx="12" cy="12" r="11"/><path d="M1 12h22M12 1c3.5 3.5 3.5 18.5 0 22M12 1c-3.5 3.5-3.5 18.5 0 22" fill="none" stroke="var(--rose)" stroke-width="1.5"/></svg>
      www.quelm.com.au
    </li>
  </ul>

  <ul class="social-list">
    <li><span class="social-dot"></span>@quelmjewellery</li>
    <li><span class="social-dot"></span>quelm_jewellery</li>
  </ul>

  <div class="founder-wordmark">QUELM</div>
</section>

<section class="card card--brand">
  <div class="brand-lockup">
    <span class="brand-mark"></span>
    <div class="brand-wordmark">QUELM</div>
  </div>
</section>

</body>
</html>
```